Food item ad for Copper Lantern Restaurant

We need visual appealing poster for our restaurant food items, for 6 categories.
1. kebabs
-tandoori chicken tikka
- tandoori 1/2 chicken
-chicken seekh
- Chaplee chicken
- Multani lamb
- lamb bouti
- lamb chops
2. Meat lover gravy dishes
- Kadai chicken masala
- butter chicken boneless
- butter chicken
- Multani kofta curry
- lamb curry
- afghani haryali lamb
3. Try this @ Copper lantern
- lamb Palou
- keema mantu
- meat thali
- kebob wraps
- chicken rolls
- sweet rice
- keema lasagna
- Romani roti
4. For vegetarian lovers
- 8 or 9 items pick n choose thali
- vegitarian
- vegitarian mantu
- aloo tikki cholay
- aloo tikki burger
- vada pav
- pav bhaji
- mix veg pakoras
5. Snakers
- sweet BBQ corn on the cob
- cassava fried
- cassava baked
- bhel puri
- sev puri
- chaat papri
- pain puri
6. Hot n cold
- Kashmiri tea. Mango milk shake
- Indian masala tea. Lessi
- English tea. Fresh juices
- green tea Fresh lime soda
- Indian style coffee Mint lime soda
We need six poster 1 for each category
it can be simple and similar theme in all six posters
the idea is to introduce the menu from my 2 Feet x 4 feet poster hanging from the window
facing the street
you go to the website:
pls take out 8-9 items in vegetarian lovers and also the word vegetarian
Industry/Entity Type
Restaurant
Requirements
Must have
- Copper lantern chef logo attached
Some food graphics
- kebabs
- rice
- Romani roti
-Naan
Kitchen equipment graphics
- tandoor ( Indian clay oven )
-Grill
Fire, charcoal, spice ,lime etc
Copper lantern color theme ,,,,,see attachments
food item names to give customer info about the menu

```html
<!DOCTYPE html>
<html lang="en">
<head>
<meta charset="utf-8">
<title>Kebabs – Copper Lantern Restaurant</title>
<link href="https://fonts.googleapis.com/css2?family=Federo&family=Kurale&family=Cinzel:wght@400&display=swap" rel="stylesheet">
<style>
  :root {
    --page-bg: #e9e9e9;
    --poster-dark: #1b0c05;
    --photo-red: #6e1a0c;
    --photo-ember: #b3441a;
    --photo-brown: #3a1c0c;
    --cream: #fcf6e2;
    --gold: #e8b92a;
    --gold-light: #ffe27a;
    --gold-deep: #9c6a08;
    --menu-white: #fffaf0;
  }
  * { margin: 0; padding: 0; box-sizing: border-box; }
  html, body {
    width: 1200px;
    height: 848px;
    overflow: hidden;
    background: var(--page-bg);
  }
  .poster {
    position: absolute;
    left: 423px;
    top: 66px;
    width: 354px;
    height: 715px;
    overflow: hidden;
    background: var(--poster-dark);
  }
  .food-photo {
    position: absolute;
    inset: 0 0 120px 0;
    background:
      radial-gradient(ellipse 60% 35% at 85% 15%, var(--photo-ember) 0%, transparent 70%),
      radial-gradient(ellipse 55% 30% at 15% 50%, #8a3a16 0%, transparent 75%),
      radial-gradient(ellipse 50% 25% at 80% 80%, #5a140a 0%, transparent 75%),
      linear-gradient(180deg, var(--photo-red) 0%, var(--photo-brown) 45%, var(--poster-dark) 100%);
  }
  .brand-panel {
    position: absolute;
    left: 72px;
    top: 0;
    width: 210px;
    height: 210px;
    background: var(--cream);
    border: 2px solid var(--gold);
    outline: 3px solid var(--cream);
    display: flex;
    flex-direction: column;
    align-items: center;
    justify-content: flex-end;
    padding-bottom: 18px;
  }
  .brand-name {
    font-family: "Kurale", serif;
    font-size: 22px;
    color: var(--gold-deep);
    letter-spacing: 0.5px;
    white-space: nowrap;
  }
  .brand-tagline {
    font-family: "Kurale", serif;
    font-size: 8px;
    color: #5a3a10;
    margin-top: 2px;
    letter-spacing: 1px;
  }
  .category-title {
    position: absolute;
    top: 240px;
    left: 0;
    width: 100%;
    text-align: center;
    font-family: "Federo", sans-serif;
    font-size: 92px;
    line-height: 1;
    letter-spacing: 1px;
    color: var(--gold);
    background: linear-gradient(180deg, var(--gold-light) 0%, var(--gold) 55%, var(--gold-deep) 100%);
    -webkit-background-clip: text;
    background-clip: text;
    -webkit-text-fill-color: transparent;
  }
  .menu-list {
    position: absolute;
    top: 352px;
    left: 0;
    width: 100%;
    list-style: none;
    text-align: center;
    font-family: "Kurale", serif;
    font-size: 22px;
    line-height: 33.5px;
    color: var(--menu-white);
    text-shadow: 0 0 4px #000, 0 0 8px #000;
  }
  .gold-wave {
    position: absolute;
    left: 0;
    top: 575px;
    width: 354px;
    height: 70px;
  }
  .footer-band {
    position: absolute;
    left: 0;
    bottom: 0;
    width: 100%;
    height: 90px;
    background: linear-gradient(180deg, #2a1606 0%, var(--poster-dark) 100%);
  }
  .website {
    position: absolute;
    left: 0;
    bottom: 18px;
    width: 100%;
    text-align: center;
    font-family: "Cinzel", serif;
    font-size: 12px;
    letter-spacing: 3.5px;
    color: var(--menu-white);
    text-transform: lowercase;
  }
</style>
</head>
<body>
  <main class="poster">
    <div class="food-photo" role="img" aria-label="Grilled kebabs, tandoori chicken and naan over glowing charcoal"></div>

    <div class="brand-panel">
      <span class="brand-name">Copper Lantern</span>
      <span class="brand-tagline">fast · fresh</span>
    </div>

    <h1 class="category-title">KEBABS</h1>

    <ul class="menu-list">
      <li>tandoori chicken tikka</li>
      <li>tandoori 1/2 chicken</li>
      <li>chicken seekh</li>
      <li>Chaplee chicken</li>
      <li>Multani lamb</li>
      <li>lamb bouti</li>
      <li>lamb chops</li>
    </ul>

    <div class="footer-band"></div>

    <svg class="gold-wave" viewBox="0 0 354 70" aria-hidden="true">
      <defs>
        <linearGradient id="goldFill" x1="0" y1="0" x2="0" y2="1">
          <stop offset="0" stop-color="#ffe27a"/>
          <stop offset="0.5" stop-color="#e8b92a"/>
          <stop offset="1" stop-color="#9c6a08"/>
        </linearGradient>
      </defs>
      <path d="M0 28 Q90 10 177 36 Q264 10 354 28 L354 44 Q264 26 177 52 Q90 26 0 44 Z" fill="url(#goldFill)"/>
      <path d="M0 50 Q90 34 177 58 Q264 34 354 50" fill="none" stroke="#e8b92a" stroke-width="2"/>
      <path d="M0 18 Q90 2 177 26 Q264 2 354 18" fill="none" stroke="#9c6a08" stroke-width="1.5"/>
    </svg>

    <p class="website">www.mycopperlantern.com</p>
  </main>
</body>
</html>
```